K.T.L Electrical Services Pty Ltd

Electrical contracting business. I have a base for the design which i like. The contact number needs to be changed to 0431862957 and the O made more solid and level with the rest of the letters. If you have any other ideas of what would make it better I'm happy to see them.

The back side to be written as dot points with the following:
- Residential & Commercial
- Maintenance
- PV & Battery servicing
- EV Chargers

```html
<!DOCTYPE html>
<html lang="en">
<head>
<meta charset="utf-8">
<title>K.T.L Electrical Services – Business Cards</title>
<link href="https://fonts.googleapis.com/css2?family=Montserrat:wght@400;500;700&display=swap" rel="stylesheet">
<style>
  :root {
    --backdrop: #3b3b3d;
    --card: #060606;
    --accent: #8fa8ad;
    --ink-light: #e9eeef;
    --rule: #b9c3c5;
  }
  * { box-sizing: border-box; margin: 0; padding: 0; }
  html, body {
    width: 1200px; height: 694px; overflow: hidden;
    background: var(--backdrop);
    font-family: "Montserrat", sans-serif;
  }
  .canvas { position: relative; width: 1200px; height: 694px; }

  .card {
    position: absolute;
    width: 540px; height: 310px;
    background: var(--card);
    border-radius: 24px;
    overflow: hidden;
  }
  .card--front { left: 36px; top: 192px; }
  .card--back  { left: 624px; top: 192px; }

  /* Company name set as plain text with one plain mark */
  .company {
    display: flex; align-items: center; gap: 12px;
    color: var(--accent); font-weight: 500; white-space: nowrap;
  }
  .company__mark {
    flex: none; border-radius: 50%; background: var(--accent);
  }

  /* Front */
  .front__company {
    position: absolute; left: 0; right: 0; top: 96px;
    justify-content: center; font-size: 30px;
  }
  .front__company .company__mark { width: 22px; height: 22px; }

  .front__services {
    position: absolute; left: 0; right: 0; top: 178px;
    text-align: center; color: var(--accent);
    font-weight: 500; font-size: 18px; line-height: 1.5;
  }
  .front__services .dot { margin: 0 6px 0 14px; }
  .front__services .dot:first-child { margin-left: 0; }

  /* Back */
  .back__company {
    position: absolute; right: 34px; top: 34px;
    font-size: 18px; gap: 10px;
  }
  .back__company .company__mark { width: 14px; height: 14px; }

  .back__person { position: absolute; left: 34px; top: 112px; }
  .person__name { color: var(--accent); font-weight: 700; font-size: 26px; line-height: 1.2; }
  .person__role { color: var(--ink-light); font-weight: 400; font-size: 15px; margin-top: 4px; }

  .back__rule {
    position: absolute; left: 34px; right: 34px; top: 186px;
    height: 1px; background: var(--rule);
  }

  .back__contacts {
    position: absolute; left: 34px; top: 204px;
    list-style: none; color: var(--ink-light);
    font-size: 15px; line-height: 1;
  }
  .back__contacts li { display: flex; align-items: center; gap: 12px; height: 28px; }
  .back__contacts svg { width: 16px; height: 16px; fill: var(--accent); flex: none; }

  .back__address {
    position: absolute; right: 34px; top: 208px;
    text-align: right; color: var(--ink-light);
    font-size: 15px; line-height: 1.6; font-style: normal;
  }
</style>
</head>
<body>
<main class="canvas">

  <section class="card card--front" aria-label="Business card front">
    <div class="company front__company">
      <span class="company__mark" aria-hidden="true"></span>
      <span class="company__name">K.T.L Electrical Services P/L</span>
    </div>
    <div class="front__services">
      <div><span class="dot">•</span>Residential &amp; Commercial<span class="dot">•</span>Maintenance</div>
      <div><span class="dot">•</span>PV &amp; Battery servicing<span class="dot">•</span>EV Chargers</div>
    </div>
  </section>

  <section class="card card--back" aria-label="Business card back">
    <div class="company back__company">
      <span class="company__mark" aria-hidden="true"></span>
      <span class="company__name">K.T.L Electrical Services P/L</span>
    </div>

    <div class="back__person">
      <div class="person__name">Daniel Reeves</div>
      <div class="person__role">Owner</div>
    </div>

    <div class="back__rule"></div>

    <ul class="back__contacts">
      <li>
        <svg viewBox="0 0 24 24" aria-hidden="true"><path d="M6.6 10.8a15.1 15.1 0 0 0 6.6 6.6l2.2-2.2a1 1 0 0 1 1-.25 11.4 11.4 0 0 0 3.6.57 1 1 0 0 1 1 1V20a1 1 0 0 1-1 1A17 17 0 0 1 3 4a1 1 0 0 1 1-1h3.5a1 1 0 0 1 1 1c0 1.25.2 2.45.57 3.57a1 1 0 0 1-.25 1z"/></svg>
        0431 862 957
      </li>
      <li>
        <svg viewBox="0 0 24 24" aria-hidden="true"><path d="M2 5h20v14H2z M4 7v.5l8 5 8-5V7z" fill-rule="evenodd"/></svg>
        info@ktlelectrical.com.au
      </li>
      <li>
        <svg viewBox="0 0 24 24" aria-hidden="true"><path d="M12 2a10 10 0 1 0 0 20 10 10 0 0 0 0-20zm0 2c.9 0 2.2 2 2.7 5H9.3C9.8 6 11.1 4 12 4zM4.3 11h3a16 16 0 0 0 0 2h-3a8 8 0 0 1 0-2zm5 0h5.4a14 14 0 0 1 0 2H9.3a14 14 0 0 1 0-2zm7.4 0h3a8 8 0 0 1 0 2h-3a16 16 0 0 0 0-2zM9.3 15h5.4c-.5 3-1.8 5-2.7 5s-2.2-2-2.7-5z"/></svg>
        www.ktlelectrical.com.au
      </li>
    </ul>

    <address class="back__address">
      18 Harlow Street, Brookvale<br>
      NSW 2100, Australia
    </address>
  </section>

</main>
</body>
</html>
```